Organic Chemistry Book Cover Design

Hi, I have a book on Brindlecart titled "71 Shortcuts for Mastering Lab Reactions". As you will see if you look on Brindlecart, I designed the cover myself (please don't hold it against me...i have also attached the current cover here). I would like a cover re-design please. I would like the background to be black and for the cover to contain the text that is already on the current cover. I can supply images of very cool-looking molecules if that helps. It needs to be for a 7"x10" book, and must follow the guidelines used by PrintHollow (template attached) The final design should WOW the 18-24 year old crowd. Thanks so much!

Target Market(s)

college students, organic chemistry students

Font styles to use
Serif
Other font styles liked:
• anything else you think might look good

Colors
000000

Requirements
Must have
• black background, must use template provided, use ad copy already on previous cover provided.
Should not have
• any real-life pictures (clip-art of real humans)

```html
<!DOCTYPE html>
<html lang="en">
<head>
<meta charset="utf-8">
<title>Organic Chemistry: 71 Shortcuts for Mastering Lab Reactions — Cover</title>
<link rel="stylesheet" href="https://fonts.googleapis.com/css2?family=Cabin+Sketch:wght@400;700&family=Open+Sans:wght@400;600;700&display=swap">
<style>
  :root {
    --stage: #e9e9e9;
    --board: #141414;
    --board-edge: #1f1f1f;
    --chalk: #ececec;
    --chalk-soft: #bdbdbd;
    --yellow: #e7c31c;
  }
  * { box-sizing: border-box; margin: 0; padding: 0; }
  html, body {
    width: 1200px; height: 1200px; overflow: hidden;
    background: radial-gradient(circle at 50% 45%, #ffffff 0%, var(--stage) 75%);
  }
  .stage {
    position: relative; width: 1200px; height: 1200px;
    display: flex; justify-content: center; align-items: center; gap: 40px;
  }
  .cover {
    position: relative; width: 490px; height: 700px;
    background: radial-gradient(ellipse at 40% 35%, var(--board-edge) 0%, var(--board) 70%);
    box-shadow: 0 10px 30px rgba(0,0,0,.25);
    color: var(--chalk);
    font-family: "Open Sans", sans-serif;
    overflow: hidden;
  }
  .chalk { font-family: "Cabin Sketch", cursive; text-transform: uppercase; line-height: 1; }

  /* front */
  .front__kicker { position: absolute; top: 62px; left: 0; right: 0; text-align: center; font-size: 40px; color: var(--chalk); }
  .front__title { position: absolute; top: 112px; left: 20px; right: 20px; text-align: center; font-size: 52px; font-weight: 700; color: var(--yellow); line-height: 1.02; }
  .front__art { position: absolute; top: 292px; left: 75px; width: 340px; height: 215px; border-radius: 40px;
    background: radial-gradient(ellipse at center, rgba(231,195,28,.22) 0%, rgba(236,236,236,.08) 55%, transparent 75%); }
  .front__lead { position: absolute; top: 528px; left: 0; right: 0; text-align: center; font-size: 34px; }
  .front__topics { position: absolute; top: 572px; left: 14px; right: 14px; text-align: center; font-size: 16px; color: var(--yellow); line-height: 1.25; white-space: nowrap; }
  .front__author { position: absolute; bottom: 24px; left: 0; right: 0; text-align: center; font-size: 13px; color: var(--chalk-soft); }

  /* back */
  .back__eyebrow { position: absolute; top: 60px; left: 48px; font-size: 13px; font-weight: 700; line-height: 1.35; text-transform: uppercase; }
  .back__title { position: absolute; top: 108px; left: 48px; font-size: 28px; color: var(--yellow); line-height: 1.08; }
  .back__icon { position: absolute; top: 36px; right: 30px; width: 100px; height: 100px; border-radius: 30px;
    background: radial-gradient(ellipse at center, rgba(236,236,236,.16) 0%, transparent 70%); }
  .back__intro { position: absolute; top: 232px; left: 48px; right: 40px; font-size: 14px; line-height: 1.35; }
  .back__list { position: absolute; top: 296px; left: 48px; right: 30px; list-style: none; font-size: 14px; line-height: 1.55; }
  .back__list li::before { content: "\2022"; margin-right: 6px; }
  .back__art { position: absolute; top: 440px; left: 60px; width: 380px; height: 160px; border-radius: 40px;
    background: radial-gradient(ellipse at center, rgba(236,236,236,.14) 0%, transparent 72%); }
  .back__footer { position: absolute; bottom: 36px; left: 48px; width: 240px; font-size: 13px; line-height: 1.4; }
</style>
</head>
<body>
<main class="stage">
  <section class="cover front">
    <p class="front__kicker chalk">Organic Chemistry:</p>
    <h1 class="front__title chalk">71 Shortcuts for Mastering Lab Reactions</h1>
    <div class="front__art" role="img" aria-label="Chalk-drawn ball-and-stick molecule model with yellow and white atoms"></div>
    <p class="front__lead chalk">Easy-to-understand</p>
    <p class="front__topics chalk">Help with: Reactions | Synthesis | Mechanisms |<br>Spectra | Reagent | Study Methods<br>...and everything else in organic chemistry</p>
    <p class="front__author">Written by LabShortcutsPress.com</p>
  </section>

  <section class="cover back">
    <p class="back__eyebrow">The perfect companion<br>to your lecture textbook</p>
    <h2 class="back__title chalk">Organic Chemistry:<br>71 Shortcuts for<br>Mastering Lab Reactions</h2>
    <div class="back__icon" role="img" aria-label="Small chalk-drawn molecule sketch"></div>
    <p class="back__intro">Learn all of the tricks and secrets to organic chemistry that your professors won't tell you, including:</p>
    <ul class="back__list">
      <li>Tricks for solving synthesis problems</li>
      <li>Easy to understand mechanism help</li>
      <li>Helpful (but little-known) reactions</li>
      <li>Clues hidden within each problem</li>
      <li>Shortcuts to the most difficult problems</li>
      <li>See what to memorize vs. what to learn</li>
    </ul>
    <div class="back__art" role="img" aria-label="Large chalk-drawn ball-and-stick molecule model"></div>
    <p class="back__footer">Perfect for organic chemistry students of all levels and those studying for the MedBoard exam</p>
  </section>
</main>
</body>
</html>
```